Events Calendar and Event Reminder Postcard Design

We need a Calendar of Events and an Event Reminder Postcard that utilize the same design look to create a uniform branding appearance. The design format for the 11" x 17" calendar page should be somewhat similar to the attached calendar sample, but not exactly the same. The 4.25" x 5.5" (4 up on an 8.5"x11" sheet) postcard needs to be able to accommodate the amount of information referenced in the attached example of our existing event reminder postcard. Our logo has been uploaded and should be included on both pieces as well. Prefer Adobe Illustrator files.

Target Market(s)

PJR Membership

Industry/Entity Type

Events

Font styles to use
Serif
Sans Serif

Requirements
Must have
• See Description and the attached sample files. Prefer Adobe InDesign files
Should not have
• Should not be cartoonish in nature

```html
<!DOCTYPE html>
<html lang="en">
<head>
<meta charset="utf-8">
<title>PJR 2018 Calendar of Events</title>
<link rel="stylesheet" href="https://fonts.googleapis.com/css2?family=Archivo:wght@400;600;700;800;900&family=Questrial&display=swap">
<style>
:root{
  --panel:#cbd6d1;
  --green:#5b9e85;
  --red:#d41f2a;
  --ink:#3c4741;
  --dark:#46524b;
  --white:#ffffff;
  --paper:#f3f6f4;
  --ghost:rgba(60,71,65,0.07);
}
*{margin:0;padding:0;box-sizing:border-box}
html,body{width:1200px;height:2362px;overflow:hidden;background:var(--white)}
body{position:relative;font-family:"Questrial",Arial,sans-serif;color:var(--ink)}

.calendar{position:absolute;left:28px;top:34px;width:1127px;height:1760px;background:var(--panel)}
.brand{position:absolute;left:180px;top:80px;width:155px;text-align:center}
.brand-mark{font-family:"Archivo",Arial,sans-serif;font-weight:900;font-size:66px;line-height:1;color:var(--dark);letter-spacing:2px}
.brand-name{font-family:"Archivo",Arial,sans-serif;font-weight:700;font-size:14px;line-height:1.1;color:var(--green);margin-top:6px}
.brand-sub{font-family:"Archivo",Arial,sans-serif;font-weight:700;font-size:7px;color:var(--dark);margin-top:3px;letter-spacing:.3px}

.title-year{position:absolute;left:350px;top:120px;font-family:"Archivo",Arial,sans-serif;font-weight:900;font-size:50px;line-height:1;color:var(--paper)}
.title-main{position:absolute;left:348px;top:170px;font-family:"Archivo",Arial,sans-serif;font-weight:600;font-size:56px;line-height:1;letter-spacing:-2.5px;color:var(--red)}
.title-rule{position:absolute;left:350px;top:232px;width:490px;height:6px;background:var(--paper);border-radius:3px}

.ghost{position:absolute;left:240px;top:650px;font-family:"Archivo",Arial,sans-serif;font-weight:900;font-size:300px;line-height:1;color:var(--ghost);letter-spacing:10px}

.divider{position:absolute;top:341px;width:2px;height:1320px;background:var(--green)}
.divider.one{left:403px}
.divider.two{left:738px}

.month{position:absolute;width:300px}
.month h2{font-family:"Archivo",Arial,sans-serif;font-weight:800;font-size:22px;letter-spacing:.5px;color:var(--green);line-height:1}
.month .rule{height:5px;background:var(--paper);border-radius:3px;margin:14px 0 20px -2px;width:305px}
.event{display:flex;font-size:18.5px;line-height:21.6px;margin-bottom:20px}
.event .day{width:83px;flex:none;color:var(--red);font-size:16px}
.event p{color:var(--ink)}

.c1{left:81px}.c2{left:420px}.c3{left:753px}

.postcard{position:absolute;left:590px;top:1850px;width:593px;height:494px;background:var(--white)}
.pc-brand{position:absolute;left:27px;top:52px;width:96px;text-align:center}
.pc-brand .brand-mark{font-size:40px}
.pc-brand .brand-name{font-size:9px;margin-top:3px}
.pc-brand .brand-sub{font-size:5px}
.pc-head{position:absolute;left:140px;top:54px;font-family:"Archivo",Arial,sans-serif;font-weight:700;font-size:33px;letter-spacing:10.5px;color:var(--green);line-height:1}
.pc-sub{position:absolute;left:160px;top:96px;font-family:"Archivo",Arial,sans-serif;font-weight:700;font-size:14.5px;color:var(--dark)}
.pc-badge{position:absolute;left:78px;top:147px;width:110px;height:110px;border-radius:50%;background:var(--dark);color:var(--white);text-align:center;font-family:"Archivo",Arial,sans-serif;padding-top:22px}
.pc-badge .free{font-weight:800;font-size:20px;letter-spacing:7px;padding-left:7px}
.pc-badge .who{font-weight:700;font-size:10px;line-height:1.25;margin-top:4px}
.pc-badge .note{font-size:7px;font-weight:600}
.pc-copy{position:absolute;left:205px;top:140px;width:335px;text-align:center;font-family:"Archivo",Arial,sans-serif;font-size:13px;line-height:17.2px;color:var(--dark)}
.pc-partner{position:absolute;left:27px;top:282px;font-family:"Archivo",Arial,sans-serif;font-weight:800;font-size:26px;color:#4caf2a;letter-spacing:-1px}
.pc-when{position:absolute;left:110px;top:324px;font-family:"Archivo",Arial,sans-serif;font-weight:700;font-size:17px;color:var(--dark)}
.pc-where{position:absolute;left:110px;top:346px;font-family:"Archivo",Arial,sans-serif;font-size:16px;color:var(--dark)}
.pc-rule{position:absolute;left:0;top:376px;width:593px;height:5px;background:var(--green);opacity:.55;border-radius:3px}
.pc-band{position:absolute;left:0;top:386px;width:593px;height:108px;background:var(--panel);text-align:center;font-family:"Archivo",Arial,sans-serif}
.pc-band .call{color:var(--white);font-size:16px;margin-top:18px;line-height:19px}
.pc-band .url{color:var(--red);font-weight:800;font-size:21px;margin-top:4px}
</style>
</head>
<body>

<section class="calendar">
  <div class="brand">
    <div class="brand-mark">PJR</div>
    <div class="brand-name">Pine Junction<br>Residential</div>
    <div class="brand-sub">OF CEDAR &amp; LINN COUNTIES</div>
  </div>
  <div class="title-year">2018</div>
  <h1 class="title-main">Calendar of Events</h1>
  <div class="title-rule"></div>

  <div class="ghost" aria-hidden="true">PJR</div>

  <div class="divider one"></div>
  <div class="divider two"></div>

  <div class="month c1" style="top:370px">
    <h2>JANUARY</h2><div class="rule"></div>
    <div class="event"><span class="day">1</span><p>Lorem ipsum dolor sit<br>amet, consectetuer<br>adipiscing elit, sed</p></div>
    <div class="event"><span class="day">15</span><p>Lorem ipsum dolor sit<br>amet, consectetuer<br>adipiscing elit, sed<br>diam nonummy nibh<br>euismod tincidunt ut<br>laoreet dolore magna<br>aliquam erat volutpat.</p></div>
    <div class="event"><span class="day">20</span><p>Lorem ipsum dolor sit<br>amet, consectetuer<br>adipiscing elit, sed</p></div>
  </div>
  <div class="month c1" style="top:756px">
    <h2>FEBRUARY</h2><div class="rule"></div>
    <div class="event"><span class="day">2</span><p>Lorem ipsum dolor sit<br>amet, consectetuer<br>adipiscing elit, sed</p></div>
    <div class="event"><span class="day">8</span><p>Lorem ipsum dolor sit<br>amet, consectetuer<br>adipiscing elit, sed</p></div>
  </div>
  <div class="month c1" style="top:1020px">
    <h2>MARCH</h2><div class="rule"></div>
    <div class="event"><span class="day">23</span><p>Lorem ipsum dolor sit<br>amet, consectetuer<br>adipiscing elit, sed</p></div>
    <div class="event"><span class="day">24</span><p>Lorem ipsum dolor sit<br>amet, consectetuer<br>adipiscing elit, sed</p></div>
    <div class="event"><span class="day">30</span><p>Lorem ipsum dolor sit<br>amet, consectetuer<br>adipiscing elit, sed</p></div>
  </div>
  <div class="month c1" style="top:1367px">
    <h2>APRIL</h2><div class="rule"></div>
    <div class="event"><span class="day">10</span><p>Lorem ipsum dolor sit<br>amet, consectetuer<br>adipiscing elit, sed</p></div>
    <div class="event"><span class="day">18</span><p>Lorem ipsum dolor sit<br>amet, consectetuer<br>adipiscing elit, sed<br>diam nonummy nibh<br>euismod tincidunt ut<br>laoreet dolore magna<br>aliquam erat volutpat.</p></div>
  </div>

  <div class="month c2" style="top:370px">
    <h2>MAY</h2><div class="rule"></div>
    <div class="event"><span class="day">1</span><p>Lorem ipsum dolor sit<br>amet, consectetuer<br>adipiscing elit, sed</p></div>
    <div class="event"><span class="day">15</span><p>Lorem ipsum dolor sit<br>amet, consectetuer<br>adipiscing elit, sed<br>diam nonummy nibh<br>euismod tincidunt ut<br>laoreet dolore magna<br>aliquam erat volutpat.</p></div>
    <div class="event"><span class="day">19</span><p>Lorem ipsum dolor sit<br>amet, consectetuer<br>adipiscing elit, sed</p></div>
  </div>
  <div class="month c2" style="top:775px">
    <h2>JUNE</h2><div class="rule"></div>
    <div class="event"><span class="day">5</span><p>Lorem ipsum dolor sit<br>amet, consectetuer<br>adipiscing elit, sed</p></div>
    <div class="event"><span class="day">11</span><p>Lorem ipsum dolor sit<br>amet, consectetuer<br>adipiscing elit, sed</p></div>
  </div>
  <div class="month c2" style="top:1019px">
    <h2>JULY</h2><div class="rule"></div>
    <div class="event"><span class="day">17</span><p>Lorem ipsum dolor sit<br>amet, consectetuer<br>adipiscing elit, sed<br>diam nonummy nibh<br>euismod tincidunt ut<br>laoreet dolore magna<br>aliquam erat volutpat.<br>Ut wisi enim ad minim<br>veniam, quis nostrud</p></div>
  </div>
  <div class="month c2" style="top:1316px">
    <h2>AUGUST</h2><div class="rule"></div>
    <div class="event"><span class="day">1</span><p>Lorem ipsum dolor sit<br>amet, consectetuer<br>adipiscing elit, sed</p></div>
    <div class="event"><span class="day">15</span><p>Lorem ipsum dolor sit<br>amet, consectetuer<br>adipiscing elit, sed</p></div>
  </div>

  <div class="month c3" style="top:370px">
    <h2>SEPTEMBER</h2><div class="rule"></div>
    <div class="event"><span class="day">12</span><p>Lorem ipsum dolor sit<br>amet, consectetuer<br>adipiscing elit, sed<br>diam nonummy nibh<br>euismod tincidunt ut<br>laoreet dolore magna<br>aliquam erat volutpat.</p></div>
  </div>
  <div class="month c3" style="top:600px">
    <h2>OCTOBER</h2><div class="rule"></div>
    <div class="event"><span class="day">10</span><p>Lorem ipsum dolor sit<br>amet, consectetuer<br>adipiscing elit, sed<br>diam nonummy nibh<br>euismod tincidunt ut<br>laoreet dolore magna<br>aliquam erat volutpat.</p></div>
    <div class="event"><span class="day">16</span><p>Lorem ipsum dolor sit<br>amet, consectetuer<br>adipiscing elit, sed</p></div>
    <div class="event"><span class="day">24</span><p>Lorem ipsum dolor sit<br>amet, consectetuer</p></div>
  </div>
  <div class="month c3" style="top:1019px">
    <h2>NOVEMBER</h2><div class="rule"></div>
    <div class="event"><span class="day">23</span><p>Lorem ipsum dolor sit<br>amet, consectetuer<br>adipiscing elit, sed</p></div>
    <div class="event"><span class="day">24</span><p>Lorem ipsum dolor sit<br>amet, consectetuer<br>adipiscing elit, sed<br>diam nonummy nibh<br>euismod tincidunt ut</p></div>
  </div>
  <div class="month c3" style="top:1316px">
    <h2>DECEMBER</h2><div class="rule"></div>
    <div class="event"><span class="day">5</span><p>Lorem ipsum dolor sit<br>amet, consectetuer<br>adipiscing elit, sed</p></div>
    <div class="event"><span class="day">11</span><p>Lorem ipsum dolor sit<br>amet, consectetuer<br>adipiscing elit, sed<br>diam nonummy nibh<br>euismod tincidunt ut</p></div>
  </div>
</section>

<section class="postcard">
  <div class="pc-brand">
    <div class="brand-mark">PJR</div>
    <div class="brand-name">Pine Junction<br>Residential</div>
    <div class="brand-sub">OF CEDAR &amp; LINN COUNTIES</div>
  </div>
  <h2 class="pc-head">REGISTER TODAY</h2>
  <p class="pc-sub">for the Feb. 7th PJR Off-the-Clock at Harlow's Home Center</p>
  <div class="pc-badge">
    <div class="free">FREE</div>
    <div class="who">for the first 20<br>BUILDER MEMBERS</div>
    <div class="note">(1 per company)</div>
  </div>
  <p class="pc-copy">Join us for an exciting Off-the-Clock hosted by Harlow's Home Center on Tuesday, February 7th. Take time after your busy day to relax and meet the appliance experts to discuss your upcoming Tour home or see what's new in the appliance industry. This is not your typical Off-the-Clock as there will be lots of chances to win valuable raffle prizes all while mixing with your fellow Association</p>
  <div class="pc-partner">Harlow's</div>
  <p class="pc-when">Tuesday, February 7th | 5:00 PM to 7:30 PM</p>
  <p class="pc-where">Harlow's Home Center | 1470 Alder Creek Rd.</p>
  <div class="pc-rule"></div>
  <div class="pc-band">
    <p class="call">Call the PJR at: 555.210.4800<br>or register online at:</p>
    <p class="url">www.pjrbuilders.org</p>
  </div>
</section>

</body>
</html>
```